Business card for new speaking/consulting business
Carla Venhuizen, CRBTEQ
Bright & Fun-filled
Growth Coach, Billing Flow Advisor, Speaker
Fernhaven, CO
carla.venhuizen@postvexa.com

```html
<!DOCTYPE html>
<html lang="en">
<head>
<meta charset="utf-8">
<title>Carla Venhuizen – Business Card</title>
<link href="https://fonts.googleapis.com/css2?family=Open+Sans:wght@400;600;700&display=swap" rel="stylesheet">
<style>
  :root {
    --bg: #ececec;
    --card-white: #ffffff;
    --sky: #1ea3dc;
    --sky-light: #5cc4ee;
    --sky-deep: #0f86c4;
    --lime: #9cc93b;
    --lime-light: #c6e07a;
    --text-grey: #6d6f71;
    --text-dark: #4a4c4e;
    --rule: #c9cbcd;
  }
  * { margin: 0; padding: 0; box-sizing: border-box; }
  html, body { width: 1200px; height: 874px; overflow: hidden; }
  body {
    background: var(--bg);
    font-family: "Open Sans", Arial, sans-serif;
    position: relative;
  }
  .card {
    position: absolute;
    width: 500px;
    height: 286px;
    border-radius: 22px;
    overflow: hidden;
    box-shadow: 0 6px 18px rgba(0,0,0,0.12);
  }
  .card-front { left: 70px; top: 294px; background: var(--card-white); }
  .card-back {
    left: 630px; top: 294px;
    background: linear-gradient(160deg, var(--sky-light) 0%, var(--sky) 55%, var(--sky-deep) 100%);
  }
  .front-waves, .back-waves { position: absolute; inset: 0; width: 100%; height: 100%; }
  .brand-name {
    position: absolute;
    left: 44px; top: 46px;
    font-weight: 700;
    font-size: 30px;
    letter-spacing: 1px;
    color: var(--sky);
    line-height: 1;
    white-space: nowrap;
  }
  .person {
    position: absolute;
    left: 24px; top: 112px;
    width: 220px;
    text-align: right;
  }
  .person-name { font-size: 13px; font-weight: 600; color: var(--sky); white-space: nowrap; }
  .person-roles { font-size: 10.5px; color: var(--text-grey); line-height: 1.35; margin-top: 2px; }
  .divider {
    position: absolute;
    left: 254px; top: 110px;
    width: 1px; height: 66px;
    background: var(--rule);
  }
  .contact {
    position: absolute;
    left: 262px; top: 108px;
    list-style: none;
    font-size: 10px;
    color: var(--text-dark);
  }
  .contact li { display: flex; align-items: center; gap: 6px; line-height: 17px; white-space: nowrap; }
  .contact-icon { width: 10px; height: 10px; flex: none; }
  .web-address {
    position: absolute;
    right: 30px; bottom: 26px;
    font-size: 13px;
    letter-spacing: 1.5px;
    color: var(--card-white);
    white-space: nowrap;
  }
</style>
</head>
<body>
  <section class="card card-front" aria-label="Card front">
    <svg class="front-waves" viewBox="0 0 500 286" preserveAspectRatio="none" aria-hidden="true">
      <path d="M0 212 C 140 190, 300 232, 500 188 L 500 200 C 300 244, 140 204, 0 226 Z" fill="var(--lime)"/>
      <path d="M0 226 C 160 206, 320 246, 500 204 L 500 214 C 320 256, 160 216, 0 238 Z" fill="var(--lime-light)"/>
      <path d="M0 246 C 170 226, 330 262, 500 226 L 500 286 L 0 286 Z" fill="var(--sky)"/>
      <path d="M0 262 C 170 244, 330 276, 500 246 L 500 286 L 0 286 Z" fill="var(--sky-deep)" opacity="0.55"/>
    </svg>

    <div class="brand-name">CARLA VENHUIZEN</div>

    <div class="person">
      <p class="person-name">Carla Venhuizen, CRBTEQ</p>
      <p class="person-roles">Growth Coach, Billing<br>Flow Advisor, Speaker</p>
    </div>

    <div class="divider"></div>

    <ul class="contact">
      <li>
        <svg class="contact-icon" viewBox="0 0 10 10"><path d="M5 0.5a3 3 0 0 0-3 3c0 2.3 3 6 3 6s3-3.7 3-6a3 3 0 0 0-3-3zm0 4.2a1.2 1.2 0 1 1 0-2.4 1.2 1.2 0 0 1 0 2.4z" fill="var(--sky)"/></svg>
        Fernhaven, CO
      </li>
      <li>
        <svg class="contact-icon" viewBox="0 0 10 10"><path d="M2.2 0.8l1.6 2-1 1.2a6 6 0 0 0 3.2 3.2l1.2-1 2 1.6-0.8 1.6C5 9.4 0.6 5 0.6 1.6z" fill="var(--sky)"/></svg>
        (303) 555-0148
      </li>
      <li>
        <svg class="contact-icon" viewBox="0 0 10 10"><rect x="0.5" y="2" width="9" height="6" rx="1" fill="var(--sky)"/><path d="M1 2.5l4 3 4-3" stroke="#fff" stroke-width="0.9" fill="none"/></svg>
        carla.venhuizen@postvexa.com
      </li>
      <li>
        <svg class="contact-icon" viewBox="0 0 10 10"><circle cx="5" cy="5" r="4.3" fill="none" stroke="var(--sky)" stroke-width="1.2"/><path d="M0.7 5h8.6M5 0.7c-2.4 2.6-2.4 6 0 8.6M5 0.7c2.4 2.6 2.4 6 0 8.6" stroke="var(--sky)" stroke-width="0.8" fill="none"/></svg>
        www.venhuizenspeaks.com
      </li>
    </ul>
  </section>

  <section class="card card-back" aria-label="Card back">
    <svg class="back-waves" viewBox="0 0 500 286" preserveAspectRatio="none" aria-hidden="true">
      <path d="M0 286 C 150 180, 320 120, 500 40 L 500 0 C 330 90, 160 160, 0 250 Z" fill="#ffffff" opacity="0.08"/>
    </svg>
    <p class="web-address">www.VenhuizenSpeaks.com</p>
  </section>
</body>
</html>
```